Emergency Dental Referral Company

I need a brochure to advertise my business to prospective dentists that may want to join or to dentists that may want to use this for their own patients. I also need to advertise this brochure to ER physicians who see many dental emergencies. This brochure is meant to be dual purpose: advertise our company and services to the ER physicians who then hand out the brochures to the dental emergency patients in pain. See our website for further details at www.molarquickfix.com

I will also be attaching our logo design.

Target Market(s)

Emergency Room physicians and other medical personnel who will distribute these brochures to patients in dental pain and dental emergencies

Industry/Entity Type

Business

Font styles to use
Serif
Sans Serif

Requirements
Must have
• Must be simple! Must have a call to action- inspiration to go to website. Highlight our guarantee that states "If you are not seen by a dentist in 24 hours or less, you will receive your money back. Emphasis on the logo. Must discuss how we find a dentist in your zip code in three easy steps.
• For the color- please make similar to our website of www.molarquickfix.com
Nice to have
• Would like to state that this service can see patients at any hour of the day.
Should not have
• no contact information besides the URL. www.molarquickfix.com

```html
<!DOCTYPE html>
<html lang="en">
<head>
<meta charset="utf-8">
<title>Molar Quick Fix – Emergency Dentist Flyer</title>
<link rel="stylesheet" href="https://fonts.googleapis.com/css2?family=Arimo:wght@400;700&display=swap">
<style>
  :root{
    --blue:#1f6fb8;
    --navy:#0b4a92;
    --green:#43a33f;
    --green-light:#6cbf4a;
    --ink:#4a4a4a;
    --text:#222222;
    --paper:#ffffff;
    --backdrop:#eef0f2;
    --tooth-light:#f4f6f8;
    --tooth-shade:#cfd6dc;
    --kit-red:#d9383a;
  }
  *{box-sizing:border-box;margin:0;padding:0}
  html,body{width:1200px;height:1000px;overflow:hidden;background:var(--backdrop)}
  body{font-family:"Arimo",Arial,sans-serif;position:relative}
  .flyer{position:absolute;left:280px;top:50px;width:640px;height:900px;background:var(--paper);overflow:hidden;box-shadow:0 6px 24px rgba(0,0,0,.18)}
  .block{position:absolute}
  .corner-square{left:0;top:0;width:110px;height:64px;background:var(--blue)}
  .side-band{left:0;top:84px;width:110px;height:620px;background:var(--green);display:flex;align-items:center;justify-content:center}
  .side-band span{transform:rotate(-90deg);white-space:nowrap;color:#fff;font-weight:700;font-size:40px;letter-spacing:.5px}
  .side-foot{left:0;top:724px;width:110px;height:176px;background:var(--blue)}
  .edge-strip{right:0;top:0;width:28px;height:500px;background:var(--blue)}
  .edge-accent{right:0;top:520px;width:28px;height:140px;background:var(--green)}
  .brand{left:150px;top:44px;width:440px;display:flex;align-items:center;justify-content:center;gap:16px}
  .brand-square{width:58px;height:58px;background:var(--blue)}
  .brand-name{font-weight:700;font-size:46px;color:var(--ink);letter-spacing:.5px;white-space:nowrap}
  .tagline{left:130px;top:150px;width:480px;text-align:center;font-size:15px;color:var(--text)}
  .steps-banner{left:210px;top:178px;width:320px;height:62px;background:var(--green-light);clip-path:polygon(0 12%,100% 0,100% 88%,0 100%);display:flex;align-items:center;justify-content:center;color:#fff;font-weight:700;font-size:34px;letter-spacing:.5px}
  .goto{left:130px;top:256px;width:480px;text-align:center;font-size:13px;color:var(--text)}
  .site-link{left:130px;top:276px;width:480px;text-align:center;font-size:20px;font-weight:700;color:var(--navy)}
  .artwork{left:132px;top:340px;width:150px;height:170px;border-radius:6px;background:linear-gradient(135deg,var(--tooth-light) 0%,var(--tooth-shade) 62%,var(--kit-red) 100%)}
  .step{position:absolute;display:flex;align-items:center;gap:18px;font-size:15px;color:var(--text);white-space:nowrap}
  .step-num{flex:none;width:42px;height:42px;border-radius:50%;background:var(--navy);color:#fff;font-weight:700;font-size:22px;display:flex;align-items:center;justify-content:center}
  .step-1{left:295px;top:335px}
  .step-2{left:340px;top:395px}
  .step-3{left:385px;top:455px}
  .guarantee{left:130px;top:560px;width:470px;height:170px;background:var(--navy);color:#fff;text-align:center;padding-top:26px}
  .guarantee svg{display:block;margin:0 auto 18px}
  .guarantee p{font-weight:700;font-size:19px;line-height:1.3}
  .footer-band{left:130px;top:750px;width:510px;height:150px;background:var(--navy);display:flex;align-items:center;justify-content:center}
  .footer-band span{color:#fff;font-size:17px;letter-spacing:5px}
</style>
</head>
<body>
  <main class="flyer">
    <div class="block corner-square"></div>
    <div class="block side-band"><span>Your Emergency Dentist</span></div>
    <div class="block side-foot"></div>
    <div class="block edge-strip"></div>
    <div class="block edge-accent"></div>

    <header class="block brand">
      <div class="brand-square"></div>
      <div class="brand-name">Molar Quick Fix</div>
    </header>

    <p class="block tagline">Find a dentist at any time of the day in</p>
    <div class="block steps-banner">3 EASY STEPS</div>
    <p class="block goto">go to</p>
    <p class="block site-link">www.molarquickfix.com</p>

    <div class="block artwork" role="img" aria-label="Illustration of a white tooth beside a red first aid kit"></div>

    <div class="step step-1"><span class="step-num">1</span><span>Fill out a form</span></div>
    <div class="step step-2"><span class="step-num">2</span><span>Find a dentist</span></div>
    <div class="step step-3"><span class="step-num">3</span><span>Get your appointment</span></div>

    <section class="block guarantee">
      <svg width="44" height="36" viewBox="0 0 44 36" aria-hidden="true"><path d="M3 19 L16 31 L41 4" fill="none" stroke="#fff" stroke-width="7" stroke-linecap="round" stroke-linejoin="round"/></svg>
      <p>If you are not seen by a dentist in 24 hours or less,<br>you will receive your money back!</p>
    </section>

    <footer class="block footer-band"><span>www.molarquickfix.com</span></footer>
  </main>
</body>
</html>
```